Website Redesign for Pet Services Facility

We are looking to redesign our current website. The website must be designed in Wix so we can go in and easily edit throughout the life of the website. Design must be professional, simplistic and informative.

Our current website can be found at: www.pawlanelodge.com

I would like the new site to be on one scrolling page. Sections to include:
Home page
Service teaser: Overnight Care, Grooming, Dog Daycare, Retail
An about us area with text on the left and a video on the right
Testimonial section
Overnight Section
Grooming Section
Dog Daycare Section
Retail
Meet the Team
Contact us: address, phone number, hours, etc.
Newsletter sign up and location map

A second page will be used for reservations and should include fields for.
Name, address, phone number, service: Overnight care, grooming, daycare, Arrival date, departure date, pet name, breed, special requests

Our phone number should be easily found through the pages. 'Request a Reservation' buttons should be found throughout page.

Text from our current site can be uesd as a filler for now as I will go in and finalize text when site is complete. Any photos can be used for now as I will go in and choose final photos as a later date.

I started playing with wix and started with a concept that I can share if you are interested, just let me know.

Industry/Entity Type

Pet

Number of Pages Required

2 page

Font styles to use
Sans Serif

Requirements
Must have
• 'Request a Reservation' Buttons
• Phone number easily visible
• location map
• Hours area
• Newsletter sign up

```html
<!DOCTYPE html>
<html lang="en">
<head>
<meta charset="utf-8">
<title>Paw Lane Lodge – Contact</title>
<link href="https://fonts.googleapis.com/css2?family=Roboto+Condensed:ital,wght@0,400;0,700;1,400;1,700&family=Roboto:wght@400&display=swap" rel="stylesheet">
<style>
:root{
  --team-bg:#aedee2;
  --contact-bg:#93babe;
  --footer-bg:#5c4d32;
  --footer-deep:#2d2519;
  --ink:#111;
  --white:#fff;
  --brown:#5c4d32;
  --field-border:#b9c6c8;
  --photo-tone:#4d5a3a;
  --map-tone:#ebe8e1;
}
*{box-sizing:border-box;margin:0;padding:0}
html,body{width:1200px;height:900px;overflow:hidden}
body{position:relative;font-family:"Roboto Condensed",Arial,sans-serif;color:var(--ink);background:var(--white)}
.abs{position:absolute}

/* team band */
.team{left:0;top:0;width:1200px;height:145px;background:var(--team-bg);overflow:hidden}
.team-photo{width:150px;height:150px;border-radius:50%;top:-46px;background:radial-gradient(circle at 55% 40%,#9a8a5a,var(--photo-tone) 55%,#2b3a6a 85%)}
.team-bio{top:-6px;width:215px;font-style:italic;font-size:14px;line-height:18.2px}

.divider{left:0;width:1200px;height:8px;background:var(--white)}

/* contact */
.contact{left:0;top:153px;width:1200px;height:465px;background:var(--contact-bg);box-shadow:inset 0 3px 3px rgba(0,0,0,.35)}
.label{font-size:15px;left:229px}
.field{background:var(--white);border:1px solid var(--field-border);left:229px}
.captcha{left:229px;top:339px;width:198px;height:50px;background:#f9f9f9;border:1px solid #d3d3d3;border-radius:3px}
.captcha-box{left:8px;top:14px;width:20px;height:20px;border:2px solid #c1c1c1;border-radius:2px;background:#fff}
.captcha-text{left:35px;top:17px;font-family:Roboto,Arial,sans-serif;font-size:9.5px;color:#222}
.captcha-legal{right:8px;top:38px;font-family:Roboto,Arial,sans-serif;font-size:5.5px;color:#777}
.btn{color:var(--white);font-size:15px;text-align:center;line-height:23px}
.btn-submit{left:229px;top:395px;width:60px;height:23px;background:var(--brown)}

.brand-square{left:644px;top:46px;width:100px;height:91px;background:var(--brown)}
.brand-name{left:764px;top:58px;font-size:36px;font-weight:700;color:var(--white);line-height:40px;letter-spacing:.5px}
.social{top:113px;width:27px;height:27px;background:var(--brown)}
.info{left:644px;font-size:16px;line-height:18px}
.info a{color:var(--brown);text-decoration:underline}
.hours-day{left:644px;font-size:16px}
.hours-time{left:726px;font-size:16px}
.note{left:644px;font-size:13px;font-style:italic;line-height:15px}

/* footer */
.footer{left:0;top:629px;width:1200px;height:232px;background:var(--footer-bg);box-shadow:inset 0 3px 3px rgba(0,0,0,.35)}
.foot-title{font-size:17px;font-weight:700;font-style:italic;color:var(--white);top:36px}
.links{list-style:none;font-size:11px;color:var(--white);line-height:15.6px;top:67px}
.foot-label{font-size:11px;color:var(--white)}
.foot-field{background:var(--white);border:1px solid var(--field-border)}
.btn-signup{left:699px;top:154px;width:60px;height:23px;background:var(--contact-bg);font-size:15px}
.map{left:817px;top:70px;width:173px;height:97px;background:linear-gradient(135deg,var(--map-tone),#d9d6cd);border:1px solid #d5d28a}

.copyright{left:0;top:861px;width:1200px;height:39px;background:linear-gradient(var(--footer-deep),#1c1710);color:var(--white);font-size:11px;text-align:center;line-height:39px}
</style>
</head>
<body>

<section class="team abs" aria-label="Meet the team">
  <div class="team-photo abs" style="left:222px" role="img" aria-label="Portrait photo of Marty, groomer"></div>
  <p class="team-bio abs" style="left:387px">I think this is Marty.&nbsp; He's a groomer.&nbsp; He does grooming stuff.&nbsp; Just look at him go. When he's not grooming, he enjoys...grooming.&nbsp; Okay, that's all he really likes.&nbsp; That's why he's so good at it!</p>
  <div class="team-photo abs" style="left:610px" role="img" aria-label="Portrait photo of Marty, groomer"></div>
  <p class="team-bio abs" style="left:775px">I think this is Marty.&nbsp; He's a groomer.&nbsp; He does grooming stuff.&nbsp; Just look at him go. When he's not grooming, he enjoys...grooming.&nbsp; Okay, that's all he really likes.&nbsp; That's why he's so good at it!</p>
</section>
<div class="divider abs" style="top:145px"></div>

<section class="contact abs" aria-label="Contact us">
  <span class="label abs" style="top:46px">Your Name</span>
  <div class="field abs" style="top:68px;width:363px;height:23px"></div>
  <span class="label abs" style="top:95px">Your Email</span>
  <div class="field abs" style="top:117px;width:363px;height:23px"></div>
  <span class="label abs" style="top:145px">What is your email about?</span>
  <div class="field abs" style="top:170px;width:148px;height:23px"></div>
  <span class="label abs" style="top:201px">Your Message</span>
  <div class="field abs" style="top:222px;width:363px;height:104px"></div>
  <div class="captcha abs">
    <div class="captcha-box abs"></div>
    <span class="captcha-text abs">I'm not a robot</span>
    <span class="captcha-legal abs">Privacy - Terms</span>
  </div>
  <div class="btn btn-submit abs">SUBMIT</div>

  <div class="brand-square abs"></div>
  <div class="brand-name abs">PAW LANE LODGE</div>
  <div class="social abs" style="left:888px" aria-label="Social link"></div>
  <div class="social abs" style="left:920px" aria-label="Social link"></div>
  <div class="social abs" style="left:953px" aria-label="Social link"></div>

  <p class="info abs" style="top:166px">2240 Orchard Lane | Maplewood, WI 54000</p>
  <p class="info abs" style="top:196px">P: 555-014-2772<br>F: 555-014-2775</p>
  <p class="info abs" style="top:255px">Email: <a href="#">info@pawlanelodge.com</a></p>
  <span class="hours-day abs" style="top:295px">Mon - Fri</span><span class="hours-time abs" style="top:295px">6am - 6pm</span>
  <span class="hours-day abs" style="top:313px">Sat</span><span class="hours-time abs" style="top:313px">8am - 6pm</span>
  <span class="hours-day abs" style="top:331px">Sun</span><span class="hours-time abs" style="top:331px">10am - 6pm</span>
  <p class="note abs" style="top:366px">Holiday Hours:<br>Closed on Easter Sunday, July 4th, Thanksgiving, and Dec 25th</p>
  <p class="note abs" style="top:409px">Limited hours for Memorial Day, Labor Day, and Dec 24th</p>
</section>
<div class="divider abs" style="top:620px;height:9px"></div>

<footer class="footer abs">
  <h3 class="foot-title abs" style="left:230px">QUICK LINKS</h3>
  <ul class="links abs" style="left:230px"><li>Home</li><li>About Us</li><li>Giving Back</li><li>Contact Us</li><li>Employment</li></ul>
  <ul class="links abs" style="left:318px"><li>Daycare</li><li>Overnight Care</li><li>Grooming</li><li>Shop</li></ul>

  <h3 class="foot-title abs" style="left:444px">NEWSLETTER SIGNUP</h3>
  <span class="foot-label abs" style="left:444px;top:68px">First Name</span>
  <span class="foot-label abs" style="left:607px;top:68px">Last Name</span>
  <div class="foot-field abs" style="left:444px;top:82px;width:153px;height:23px"></div>
  <div class="foot-field abs" style="left:607px;top:82px;width:153px;height:23px"></div>
  <span class="foot-label abs" style="left:444px;top:108px">Email Address</span>
  <div class="foot-field abs" style="left:444px;top:122px;width:316px;height:23px"></div>
  <div class="btn btn-signup abs">SUBMIT</div>

  <h3 class="foot-title abs" style="left:817px">LOCATION</h3>
  <div class="map abs" role="img" aria-label="Street map showing the Paw Lane Lodge location"></div>
</footer>

<div class="copyright abs">Copyright 2017 - Paw Lane Lodge</div>
</body>
</html>
```